Business Card Design for ReaL ESTATE AGENT

New Business Cards for a real estate agent in Jacksonville, FL. My specialty is urban core, historic districts but sell through out the city. Company Name is Quill and Harbor Realty a division of the Vantrell Companies. The card needs to convey an essence of professionalism, knowledge and success.

Target Market(s)

Home buyers and Sellers

Industry/Entity Type

Real Estate

Contact Information for Business Card

Double sided

Font styles to use
Sans Serif

Requirements
Must have
• My logs and photo (provided). My contact information as follows:
• Derek Holloway
• Cell 904-618-3092
• Office 904-731-6248
• Email derekholloway@mailvantor.com
Nice to have
• Tag Line - Exceptional Effort. Proven Results.

```html
<!DOCTYPE html>
<html lang="en">
<head>
<meta charset="utf-8">
<title>Derek Holloway – Business Card</title>
<link rel="stylesheet" href="https://fonts.googleapis.com/css2?family=Didact+Gothic&family=Gentium+Book+Plus&display=swap">
<style>
  :root {
    --panel-brown: #522400;
    --panel-border: #000000;
    --name-cyan: #00f5f5;
    --tagline-red: #ff1a1a;
    --contact-orange: #d45b0c;
    --brand-green: #1f7a2e;
    --subtitle-ink: #111111;
    --photo-dark: #2c3e48;
    --photo-light: #4d6470;
    --card-white: #ffffff;
  }
  html, body {
    margin: 0;
    padding: 0;
    overflow: hidden;
    background: var(--card-white);
  }
  .card {
    position: relative;
    width: 1200px;
    height: 666px;
    background: var(--card-white);
    overflow: hidden;
  }
  .agent-panel {
    position: absolute;
    left: 0;
    top: 0;
    width: 546px;
    height: 666px;
    box-sizing: border-box;
    background: var(--panel-brown);
    border: 5px solid var(--panel-border);
  }
  .agent-photo {
    position: absolute;
    left: 92px;
    top: 21px;
    width: 329px;
    height: 328px;
    background: radial-gradient(ellipse at 50% 40%, var(--photo-light), var(--photo-dark));
  }
  .agent-name {
    position: absolute;
    left: 10px;
    top: 350px;
    width: 526px;
    margin: 0;
    font-family: "Didact Gothic", sans-serif;
    font-weight: 400;
    font-size: 64px;
    letter-spacing: -4px;
    color: var(--name-cyan);
    white-space: nowrap;
    text-align: center;
  }
  .tagline {
    position: absolute;
    left: 0;
    width: 536px;
    top: 610px;
    margin: 0;
    font-family: "Gentium Book Plus", serif;
    font-size: 30px;
    letter-spacing: -1px;
    color: var(--tagline-red);
    text-align: center;
    white-space: nowrap;
  }
  .brand {
    position: absolute;
    left: 790px;
    top: 60px;
    width: 400px;
    display: flex;
    flex-direction: column;
    align-items: center;
    gap: 18px;
  }
  .brand-mark {
    width: 90px;
    height: 90px;
  }
  .brand-name {
    margin: 0;
    font-family: "Didact Gothic", sans-serif;
    font-size: 34px;
    color: var(--brand-green);
    text-align: center;
    line-height: 1.15;
  }
  .brand-division {
    position: absolute;
    left: 770px;
    top: 284px;
    width: 430px;
    margin: 0;
    font-family: "Gentium Book Plus", serif;
    font-size: 29px;
    letter-spacing: -1.2px;
    color: var(--subtitle-ink);
    text-align: right;
    white-space: nowrap;
  }
  .contact {
    position: absolute;
    left: 566px;
    top: 485px;
    width: 626px;
    margin: 0;
    font-family: "Didact Gothic", sans-serif;
    color: var(--contact-orange);
  }
  .contact-row {
    display: flex;
    justify-content: space-between;
    font-size: 50px;
    letter-spacing: -2.5px;
    line-height: 54px;
  }
  .contact-email {
    font-size: 37px;
    letter-spacing: -2px;
    line-height: 54px;
    white-space: nowrap;
  }
</style>
</head>
<body>
  <main class="card">
    <section class="agent-panel">
      <div class="agent-photo" role="img" aria-label="Portrait photo of agent Derek Holloway"></div>
      <h1 class="agent-name">Derek Holloway</h1>
      <p class="tagline">Exceptional&nbsp; Effort. Proven&nbsp; Results.</p>
    </section>

    <header class="brand">
      <svg class="brand-mark" viewBox="0 0 90 90" aria-hidden="true">
        <circle cx="45" cy="45" r="40" fill="none" stroke="var(--brand-green)" stroke-width="5"/>
      </svg>
      <p class="brand-name">Quill and Harbor Realty</p>
    </header>
    <p class="brand-division">(A division of the Vantrell Companies)</p>

    <section class="contact">
      <div class="contact-row"><span>Cell</span><span>904-618-3092</span></div>
      <div class="contact-row"><span>Office</span><span>904-731-6248</span></div>
      <div class="contact-email">Email :derekholloway@mailvantor.com</div>
    </section>
  </main>
</body>
</html>
```